Business Card Design

We are starting up a new Family run Business mainly offering a Free House Clearance service. We also offer the following chargeable services which include a Removals Service, Delivery and Collection of Items sold or purchased on Bidloft, Swapwren etc, including Motorcycles, Piano's, Furniture, Electrical appliances.
As there are a few Companies offering similar services we need to stand out and show what we do at a glance while appearing Professional and approachable
Updates

TidyNests

i  am liking some of the colours and designs so far but would like to see a few of our services listed as 1 or 2 have already done if this is possible and maybe some emphasis on the FREE House Clearance. thank you 
best regards
derek

Target Market(s)

Commercial and Domestic Tenants and Landlords aswell as Families looking for a friendly sympathetic clearance service after bereavement

Industry/Entity Type

Business

Contact Information for Business Card

TidyNests,
HouseClearance and Removals,
Marlow Dene
LM47 2QT
Tel: 07815239604
Email: enquiries@tidynests-example.info

```html
<!DOCTYPE html>
<html lang="en">
<head>
<meta charset="utf-8">
<title>TidyNests – Business Card</title>
<link rel="stylesheet" href="https://fonts.googleapis.com/css2?family=Noto+Sans:wght@400&family=Noto+Serif:wght@400;700&family=Open+Sans:wght@400&display=swap">
<style>
  :root {
    --backdrop: #6b6c70;
    --card: #f1f1f1;
    --ink: #4a4a4c;
    --ink-dark: #1f1f21;
    --accent: #f7941d;
  }
  * { margin: 0; padding: 0; box-sizing: border-box; }
  html, body { width: 1200px; height: 876px; overflow: hidden; }
  body { background: var(--backdrop); position: relative; }

  .card {
    position: absolute;
    top: 54px;
    width: 450px;
    height: 767px;
    background: var(--card);
  }
  .card--front { left: 78px; }
  .card--back { left: 672px; }

  .brand { position: absolute; left: 102px; top: 300px; }
  .brand__name {
    font-family: "Open Sans", sans-serif;
    font-weight: 400;
    font-size: 39px;
    line-height: 1;
    color: var(--ink);
    letter-spacing: 0.3px;
  }
  .brand__tagline {
    margin-top: 6px;
    font-family: "Noto Serif", serif;
    font-size: 16px;
    color: var(--ink);
  }

  .contact-list {
    position: absolute;
    left: 66px;
    top: 531px;
    list-style: none;
    font-family: "Noto Sans", sans-serif;
    font-size: 21px;
    color: var(--ink-dark);
  }
  .contact-list li {
    display: flex;
    align-items: center;
    height: 40px;
  }
  .contact-list svg {
    width: 15px;
    height: 15px;
    margin-right: 24px;
    fill: var(--accent);
    flex-shrink: 0;
  }

  .services {
    position: absolute;
    left: 0;
    width: 100%;
    top: 182px;
    text-align: center;
    font-family: "Noto Serif", serif;
    font-size: 20px;
    line-height: 28px;
    color: var(--ink);
  }
  .services__heading {
    font-weight: 700;
    margin-bottom: 57px;
  }
  .accent { color: var(--accent); }
  .services__list { list-style: none; }
  .services__list li + li { margin-top: 28px; }
</style>
</head>
<body>
  <section class="card card--front">
    <div class="brand">
      <p class="brand__name">tidy nests</p>
      <p class="brand__tagline">house clearance and removals</p>
    </div>

    <ul class="contact-list">
      <li>
        <svg viewBox="0 0 16 16" aria-hidden="true"><path d="M8 1 1 7.5h2V15h10V7.5h2z"/></svg>
        Marlow Dene LM47 2QT
      </li>
      <li>
        <svg viewBox="0 0 16 16" aria-hidden="true"><path d="M3.6 1 6 3.6 4.6 5.6c.9 2.3 3.2 4.7 5.7 5.7l2-1.5L15 12.3 13.3 15C6.9 14.6 1.4 9.1 1 2.7z"/></svg>
        07815239604
      </li>
      <li>
        <svg viewBox="0 0 16 16" aria-hidden="true"><path d="M1 3.5h14v1.2L8 9 1 4.7zM1 6.2l7 4.3 7-4.3v6.3H1z"/></svg>
        enquiries@tidynests-example.info
      </li>
      <li>
        <svg viewBox="0 0 16 16" aria-hidden="true"><circle cx="8" cy="8" r="7"/><path d="M5 4.5c1.5.3 2 1.5 1.2 2.6-.7 1 .6 2 1.8 1.6 1.1-.4 1.3 1.6.4 2.8" fill="none" stroke="#f1f1f1" stroke-width="1.2"/></svg>
        www.tidynests-example.info
      </li>
    </ul>
  </section>

  <section class="card card--back">
    <div class="services">
      <p class="services__heading"><span class="accent">C</span>ontact us for:</p>
      <ul class="services__list">
        <li>Free House Clearance</li>
        <li>Removals Service</li>
        <li>Delivery and Collection of<br>Items sold or purchased on<br>Bidloft, Swapwren etc.</li>
        <li>including Motorcycles,<br>Piano's, Furniture,<br>Electrical appliances</li>
      </ul>
    </div>
  </section>
</body>
</html>
```